Brisk Lending Benefits Summary

We are looking to put our benefits information into a summary document and make it look pretty/easy to read! I put all of the information together into a document, one tab for all of our medical plans and another for dental/vision. This document is only there as a guide. I want this to be visually appealing, so feel free to get creative with the format.

Industry/Entity Type

Mortgage Lender

Colors
31b7a3
ffcf3e

Requirements
Should not have
• I don't want a copy and pasted version of the visual I sent, with our logo attached.

```html
<!DOCTYPE html>
<html lang="en">
<head>
<meta charset="utf-8">
<title>Brisk Lending Benefits Summary</title>
<link href="https://fonts.googleapis.com/css2?family=Nunito+Sans:wght@400;600;700;800&display=swap" rel="stylesheet">
<style>
:root{
  --navy:#1c335f;
  --navy-deep:#13264b;
  --teal:#2fb0c6;
  --teal-light:#a9e1ea;
  --orange:#f4a75a;
  --label-dark:#59616c;
  --label-mid:#6d757f;
  --cell-white:#ffffff;
  --cell-grey:#ececed;
  --sub-grey:#8b939d;
  --sub-light:#cdd1d6;
  --ink:#2a2d33;
  --paper:#ffffff;
}
*{box-sizing:border-box;margin:0;padding:0}
html,body{width:1200px;height:900px;overflow:hidden}
body{background:var(--paper);font-family:"Nunito Sans",Arial,sans-serif;color:var(--ink);position:relative}
.navy-band{position:absolute;left:0;top:418px;width:1200px;height:482px;background:var(--navy)}
.brand-corner{position:absolute;right:0;top:0;width:269px;height:109px;background:var(--navy);border-bottom-left-radius:110px;display:flex;align-items:center;justify-content:flex-end;padding-right:28px}
.brand-name{color:var(--teal);font-weight:800;font-size:25px;letter-spacing:.2px}
.curve-decor{position:absolute;left:1080px;top:560px;width:120px;height:340px;background:linear-gradient(160deg,rgba(47,176,198,0) 0%,rgba(47,176,198,.35) 60%,rgba(47,176,198,.15) 100%)}
.section-icon{position:absolute}
.section-title{position:absolute;color:var(--teal);font-weight:800;font-size:37px;letter-spacing:1px}

/* Vision */
.col-head{position:absolute;display:flex;align-items:center;justify-content:center;font-size:13px;font-weight:600;border-radius:8px 8px 0 0}
.col-head.in{left:213px;top:149px;width:169px;height:56px;background:var(--orange);color:#fff;box-shadow:0 -2px 6px rgba(0,0,0,.12)}
.col-head.non{left:382px;top:168px;width:169px;height:37px;background:#dedfe1;color:var(--ink)}
.in-backdrop{position:absolute;left:213px;top:200px;width:169px;height:658px;background:var(--cell-white);border-radius:0 0 8px 8px;box-shadow:0 3px 10px rgba(0,0,0,.25)}
.vision-table{position:absolute;left:44px;top:205px;width:507px;display:grid;grid-template-columns:169px 169px 169px;grid-template-rows:87px 85px 42px 85px 86px 44px 43px 44px 43px 85px}
.cell{display:flex;flex-direction:column;justify-content:center;align-items:center;text-align:center;font-size:10px;line-height:15.5px}
.cell.grey{background:var(--cell-grey)}
.cell.in.grey{background:rgba(236,236,237,.9)}
.cell.in.white{background:transparent}
.cell.non.white{background:var(--cell-white)}
.cell .fine{font-size:8.6px;line-height:11px;padding:0 6px}
.cell.offset{padding-top:14px}
.label{background:var(--label-dark);color:#fff;display:flex;flex-direction:column;justify-content:center;padding-left:16px;font-size:10px;font-weight:700;line-height:15.5px}
.label.mid{background:var(--label-mid)}
.label.first{border-top-left-radius:8px}
.label.last{border-bottom-left-radius:8px}
.label ul{list-style:none;font-weight:400;color:#e8eaed}
.label li::before{content:"•";margin-right:5px;color:var(--teal)}
.label .small-head{font-size:8.6px}
.label .tiny{font-size:7.6px}
.vision-table .non.last{border-bottom-right-radius:8px}

/* Dental */
.dental-head{position:absolute;top:153px;height:45px;display:flex;align-items:center;justify-content:center;color:#fff;font-size:13.5px;font-weight:600;border-radius:8px 8px 0 0}
.dental-head.deductible{left:775px;width:191px;background:var(--navy-deep)}
.dental-head.coinsurance{left:967px;width:193px;background:var(--teal)}
.sub-row{position:absolute;left:775px;width:385px;height:22px;display:grid;grid-template-columns:96px 96px 96px 97px}
.sub{display:flex;align-items:center;justify-content:center;font-size:8.6px;font-weight:600}
.sub.g{background:var(--sub-grey);color:#fff}
.sub.gl{background:var(--sub-light);color:var(--ink)}
.sub.t{background:var(--teal);color:#d7f3f7}
.sub.tl{background:var(--teal-light);color:var(--ink)}
.dental-table{position:absolute;left:605px;width:555px;display:grid;grid-template-columns:170px 96px 96px 96px 97px}
.dental-table.main{top:220px;grid-template-rows:28px 28px 28px 57px 56px}
.dental-table .cell{font-weight:700;font-size:10px;border-right:1px solid #d9dbde;color:var(--ink)}
.dental-table .cell.white{background:var(--cell-white)}
.dental-table .cell.span{grid-column:2 / 6;font-weight:400;font-size:9.6px;line-height:13.5px;padding:0 12px;border-right:none}
.dental-table .label{font-size:9.8px}
.ortho-head{position:absolute;left:775px;top:417px;width:385px;height:41px;background:var(--label-mid);color:#fff;font-size:13.5px;font-weight:600;display:flex;align-items:center;justify-content:center}
.dental-table.ortho{top:480px;grid-template-rows:55px 88px}
.two-line{gap:8px}
.dental-table.ortho .cell.span{font-weight:700;font-size:10px;line-height:21px;border-bottom-right-radius:8px}
.footnotes{position:absolute;left:619px;top:709px;width:542px;color:#fff;font-size:9.6px;line-height:13px}
.footnotes p{margin-bottom:11px}
</style>
</head>
<body>
<div class="navy-band"></div>
<div class="curve-decor" role="img" aria-label="Decorative flowing teal line pattern"></div>
<div class="brand-corner"><span class="brand-name">Brisk Lending</span></div>

<!-- Vision -->
<svg class="section-icon vision-icon" style="left:58px;top:82px" width="82" height="58" viewBox="0 0 82 58" aria-hidden="true">
  <path d="M4 28 Q41 -6 78 28" fill="none" stroke="var(--teal)" stroke-width="3.5" stroke-linecap="round"/>
  <circle cx="41" cy="34" r="20" fill="none" stroke="var(--teal)" stroke-width="3.5"/>
  <circle cx="41" cy="34" r="9" fill="#f7c531"/>
</svg>
<div class="section-title" style="left:61px;top:146px">VISION</div>

<div class="col-head in">In-Network</div>
<div class="col-head non">Non-Network</div>
<div class="in-backdrop"></div>

<div class="vision-table">
  <div class="label first"><span>Co-Pay</span><ul><li>First Service Provided</li><li>Exams</li><li>Materials</li></ul></div>
  <div class="cell in white"><span>Not applicable</span><span>Exams $10.00</span><span>$25</span><span class="fine">Waived for conventional &amp; planned replacement contact lenses</span></div>
  <div class="cell non white"><span>Not applicable</span><span>Exams $10.00</span><span>$25</span><span class="fine">Waived for conventional &amp; planned replacement contact lenses</span></div>

  <div class="label mid"><span class="small-head">How Often Can I Obtain Service?*</span><ul><li>Exams</li><li>Lenses</li><li>Frames</li><li>Materials</li></ul></div>
  <div class="cell in grey offset"><span>Once/year</span><span>Once/year</span><span>Once every other year</span><span>Once/year</span></div>
  <div class="cell non grey offset"><span>Once/year</span><span>Once/year</span><span>Once every other year</span><span>Once/year</span></div>

  <div class="label"><span>Eye Exams</span></div>
  <div class="cell in white">Copay applies</div>
  <div class="cell non white">Amount over $39</div>

  <div class="label mid"><span>Lenses</span><ul><li>Single Vision</li><li>Lined Bifocal</li><li>Lined Trifocal</li><li>Lenticular</li></ul></div>
  <div class="cell in grey offset"><span>Copay applies</span><span>Copay applies</span><span>Copay applies</span><span>Copay applies</span></div>
  <div class="cell non grey offset"><span>Amount over $23</span><span>Amount over $37</span><span>Amount over $49</span><span>Amount over $64</span></div>

  <div class="label"><span>Contact Lenses</span><ul><li>Conventional</li><li class="tiny">Planned Replacement &amp; Disposable</li><li>Medically Necessary</li><li>Evaulation &amp; Fitting</li></ul></div>
  <div class="cell in white offset"><span>Amount over $130</span><span>Amount over $130</span><span>Copay applies</span><span>15% off professional fee</span></div>
  <div class="cell non white offset"><span>Amount over $100</span><span>Amount over $100</span><span>Amount over $210</span><span>Not covered</span></div>

  <div class="label mid"><span>Frames</span></div>
  <div class="cell in grey"><span>$130, 20% discount</span><span>on amount over $130</span></div>
  <div class="cell non grey">Amount over $46</div>

  <div class="label"><span>Lens &amp; Frame Allowance</span></div>
  <div class="cell in white">No discounts</div>
  <div class="cell non white">No discounts</div>

  <div class="label mid"><span>Cosmetic Extras</span></div>
  <div class="cell in grey"><span>Discounted at average</span><span>20%-25% off providers UCR</span></div>
  <div class="cell non grey">No discounts</div>

  <div class="label"><span>Laser Correction Surgery</span></div>
  <div class="cell in white"><span class="fine" style="font-size:9px;line-height:14px">Average 15% discount off usual price or 5% off promotional price</span></div>
  <div class="cell non white">No discounts</div>

  <div class="label mid last"><span>Monthly Cost**</span><ul><li>Employee</li><li>Child Cost***</li><li>Spouse/Domestic Partner Cost</li></ul></div>
  <div class="cell in grey offset"><span>$9</span><span>$7</span><span>$6</span></div>
  <div class="cell non grey offset last"><span>$9</span><span>$7</span><span>$6</span></div>
</div>

<!-- Dental -->
<svg class="section-icon dental-icon" style="left:608px;top:90px" width="78" height="62" viewBox="0 0 78 62" aria-hidden="true">
  <path d="M24 4 C14 4 12 14 15 24 C18 34 20 46 25 54 C29 58 31 50 33 42 C35 36 43 36 45 42 C47 50 49 58 53 54 C58 46 60 34 63 24 C66 14 64 4 54 4 C47 4 44 8 39 8 C34 8 31 4 24 4 Z" fill="none" stroke="var(--teal)" stroke-width="3.5" stroke-linejoin="round"/>
  <path d="M6 38 Q2 52 20 56" fill="none" stroke="var(--teal)" stroke-width="3.5" stroke-linecap="round"/>
  <path d="M72 38 Q76 52 58 56" fill="none" stroke="var(--teal)" stroke-width="3.5" stroke-linecap="round"/>
</svg>
<div class="section-title" style="left:612px;top:163px">DENTAL</div>

<div class="dental-head deductible">Calendar Year Deductible</div>
<div class="dental-head coinsurance">Coinsurance (Policy Pays)</div>
<div class="sub-row" style="top:198px">
  <div class="sub g">In-Network</div><div class="sub gl">Non-Network</div><div class="sub t">In-Network</div><div class="sub tl">Non-Network</div>
</div>

<div class="dental-table main">
  <div class="label first">Preventative</div>
  <div class="cell white">$0</div><div class="cell white">$0</div><div class="cell white">100%</div><div class="cell white">100%</div>
  <div class="label mid">Basic</div>
  <div class="cell grey">$50</div><div class="cell grey">$50</div><div class="cell grey">80%</div><div class="cell grey">80%</div>
  <div class="label">Major</div>
  <div class="cell white">$50</div><div class="cell white">$50</div><div class="cell white">50%</div><div class="cell white">50%</div>
  <div class="label mid">Combined Family Deductible</div>
  <div class="cell grey span">Max deductible 3 times the per person deductible amount. Deductibles for basic and major procedures are combined for in-network and non-network.</div>
  <div class="label last">Combined Maximum</div>
  <div class="cell white span">Maximums for preventative, basic, and major procedures combined.<br>In- network and non-network maximums are $1,000 per person.</div>
</div>

<div class="ortho-head">Orthodontia - Child</div>
<div class="sub-row" style="top:458px">
  <div class="sub g">In-Network</div><div class="sub gl">Non-Network</div><div class="sub t">In-Network</div><div class="sub tl">Non-Network</div>
</div>

<div class="dental-table ortho">
  <div class="label first" style="gap:6px"><span>Lifetime Deductible</span><span>Lifetime Maximum</span></div>
  <div class="cell white two-line"><span>$0</span><span>$1000</span></div>
  <div class="cell white two-line"><span>$0</span><span>$1000</span></div>
  <div class="cell white">50%</div>
  <div class="cell white">50%</div>
  <div class="label mid last"><span>Monthly Cost**</span><ul><li>Employee</li><li>Child Cost***</li><li>Spouse/Domestic Partner Cost</li></ul></div>
  <div class="cell grey span"><span>$40</span><span>$68</span><span>$41</span></div>
</div>

<div class="footnotes">
  <p>Limitations, exceptions and other important information are provided in the summary of benefits and coverage for each plan. In the event that the information in this summary differs from the plan description, the plan description will prevail.</p>
  <p>*Members will receive 20% off unlimited additional pairs of prescription glasses and non prescription sunglasses valid through any ClearSight doctor within 12 months of the last covered exam.</p>
  <p>**For the purpose of this document, we assume that your spouse is the same age as you and that your children are 18 years old or less. Your quoted price may change based on the actual age of your spouse and children.</p>
  <p>***Children beyond the first child are covered at no additional cost.</p>
</div>
</body>
</html>
```